I am looking for a stand-out cover that sings out to new parents. The category is very pastel with limited compelling covers that would make me want to buy a book. This book will be used often in the first 12 months of baby's life - so must be strong enough to sit on the bedside table or on the coffee table to inspire reading. It will be a popular gift - so needs to look credible, "pick-up-able" and loveable.

The Book Title is - The Cradle Compass to Infancy's Opening Seasons: Grounded, Research-Led Methods on Rest, Nourishment, Protection plus Growing Assurance
The Size is - 8.5 x 11 in
Book description to be provided to final design for inclusion
Some examples of book covers in this category attached. Thanks

```html
<!DOCTYPE html>
<html lang="en">
<head>
<meta charset="utf-8">
<title>The Cradle Compass to Infancy's Opening Seasons</title>
<link rel="stylesheet" href="https://fonts.googleapis.com/css2?family=Oswald:wght@600;700&family=Outfit:wght@500&display=swap">
<style>
  :root {
    --paper: #f6efe2;
    --ink: #262626;
    --charcoal: #2e2d2c;
    --orange: #ec5d24;
    --sage: #6b9a78;
    --sand: #e2a86a;
  }
  * { margin: 0; padding: 0; box-sizing: border-box; }
  html, body { width: 800px; height: 1200px; overflow: hidden; background: var(--paper); }
  .cover {
    position: relative;
    width: 800px;
    height: 1200px;
    background: var(--paper);
    overflow: hidden;
  }
  .decor { position: absolute; inset: 0; width: 800px; height: 1200px; }
  .title-block {
    position: absolute;
    left: 90px;
    top: 92px;
    font-family: "Oswald", "Arial Narrow", sans-serif;
    text-transform: uppercase;
    color: var(--ink);
  }
  .title-lead {
    font-size: 60px;
    font-weight: 700;
    line-height: 1;
    letter-spacing: 0.5px;
  }
  .title-main {
    font-size: 92px;
    font-weight: 700;
    line-height: 1;
    color: var(--orange);
    margin-top: 4px;
    letter-spacing: 0.5px;
  }
  .title-tail {
    font-size: 33px;
    font-weight: 600;
    line-height: 1;
    margin-top: 16px;
    letter-spacing: 0.3px;
  }
  .title-rule {
    width: 380px;
    height: 2px;
    background: var(--ink);
    margin-top: 16px;
  }
  .hero-art {
    position: absolute;
    left: 137px;
    top: 324px;
    width: 574px;
    height: 594px;
    border-radius: 46% 46% 42% 42% / 40% 40% 50% 50%;
    background: radial-gradient(circle at 48% 62%, var(--paper) 0 9%, var(--orange) 10% 27%, var(--charcoal) 28% 100%);
  }
  .subtitle-rule {
    position: absolute;
    left: 84px;
    top: 933px;
    width: 596px;
    height: 2px;
    background: var(--ink);
  }
  .subtitle {
    position: absolute;
    left: 84px;
    top: 958px;
    width: 596px;
    text-align: center;
    font-family: "Outfit", "Helvetica", sans-serif;
    font-weight: 500;
    font-size: 23px;
    line-height: 1.42;
    color: var(--ink);
  }
</style>
</head>
<body>
<main class="cover">
  <svg class="decor" viewBox="0 0 800 1200" aria-hidden="true">
    <polygon class="band-top" points="0,0 348,0 346,16 0,30" fill="var(--ink)"/>
    <rect class="block-sage" x="0" y="74" width="55" height="406" fill="var(--sage)"/>
    <polygon class="corner-orange" points="551,0 800,0 800,281" fill="var(--orange)"/>
    <g class="plus-mark" stroke="var(--ink)" stroke-width="3">
      <line x1="742" y1="49" x2="770" y2="49"/>
      <line x1="756" y1="35" x2="756" y2="63"/>
    </g>
    <polygon class="block-sand" points="722,598 800,600 800,996 718,992" fill="var(--sand)"/>
    <polygon class="corner-orange-low" points="0,1023 258,1090 289,1200 0,1200" fill="var(--orange)"/>
    <g class="dash-lines" stroke="var(--ink)" stroke-width="2">
      <line x1="0" y1="866" x2="61" y2="866"/>
      <line x1="0" y1="875" x2="43" y2="875"/>
      <line x1="703" y1="1095" x2="800" y2="1095"/>
      <line x1="719" y1="1105" x2="800" y2="1105"/>
    </g>
  </svg>

  <header class="title-block">
    <h1>
      <span class="title-lead" style="display:block">The Cradle</span>
      <span class="title-main" style="display:block">Compass</span>
      <span class="title-tail" style="display:block">To Infancy’s Opening Seasons</span>
    </h1>
    <div class="title-rule"></div>
  </header>

  <div class="hero-art" role="img" aria-label="Illustration of an adult hand with a smaller child hand and a tiny baby hand nested inside it"></div>

  <div class="subtitle-rule"></div>
  <p class="subtitle">Grounded, Research-Led Methods<br>on Rest, Nourishment, Protection<br>plus Growing Assurance</p>
</main>
</body>
</html>
```